Sales Folder for equipment company

I have a two sided folder that I would like to improve the back side, I am happy with the front side (right side attached file), but open to any suggested improvements. on the other left side I would like to feature an image of my other product line tal vine (blue) there also should be images at talvin.com and bivolle. For the business card I am thinking the photo of the two spraybooths (white equipment with doors) would be best as a backdrop and feature tal vine on the back side or if there is any decent way to super impose the blue talvine products in front of the spraybooths I would be open to that also

```html
<!DOCTYPE html>
<html lang="en">
<head>
<meta charset="utf-8">
<title>Midaxis Business Card</title>
<link rel="stylesheet" href="https://fonts.googleapis.com/css2?family=Arimo:wght@400;700&display=swap">
<style>
  :root {
    --page-bg: #1c1d22;
    --card-white: #ffffff;
    --card-black: #050505;
    --brand-red: #d9262c;
    --ink: #111111;
    --shine: #3a3a3a;
    --tool-blue: #2f55b8;
    --tool-light: #eef2fa;
  }
  * { box-sizing: border-box; margin: 0; padding: 0; }
  html, body {
    width: 1200px; height: 900px; overflow: hidden;
    background: var(--page-bg);
    font-family: "Arimo", Arial, sans-serif;
  }
  .sheet {
    position: relative; width: 1200px; height: 900px;
    display: flex; flex-direction: column; align-items: center;
    justify-content: center; gap: 30px;
  }
  .card {
    position: relative; width: 700px; height: 400px; overflow: hidden;
    box-shadow: 0 10px 30px rgba(0,0,0,.5);
  }

  /* Back side */
  .card--back {
    background: linear-gradient(115deg, var(--card-black) 0%, var(--card-black) 60%, var(--shine) 61%, #1e1e1e 100%);
  }
  .card--back .brand {
    position: absolute; left: 120px; top: 52px;
    font-weight: 700; font-size: 64px; letter-spacing: 3px;
    color: var(--card-white);
  }
  .product {
    position: absolute; width: 108px; height: 108px; border-radius: 50%;
    background: radial-gradient(circle at 50% 55%, var(--tool-blue) 0%, #6d86cc 28%, var(--tool-light) 55%, #ffffff 75%);
    border: 3px solid #9a9a9a;
  }

  /* Front side */
  .card--front { background: var(--card-white); }
  .card--front .brand {
    position: absolute; left: 0; right: 0; top: 62px; text-align: center;
    font-weight: 700; font-size: 64px; letter-spacing: 3px; color: var(--ink);
  }
  .person {
    position: absolute; right: 380px; top: 205px; text-align: right;
  }
  .person__name { font-weight: 700; font-size: 27px; color: var(--brand-red); }
  .person__role { font-size: 22px; color: var(--ink); margin-top: 6px; }
  .divider {
    position: absolute; left: 342px; top: 200px; width: 2px; height: 82px;
    background: var(--ink);
  }
  .contacts {
    position: absolute; left: 362px; top: 198px; list-style: none;
  }
  .contacts li {
    display: flex; align-items: center; gap: 12px;
    font-size: 22px; color: var(--ink); height: 29px;
  }
  .contacts svg { width: 20px; height: 20px; fill: var(--brand-red); flex: none; }
  .address-band {
    position: absolute; left: 0; right: 0; bottom: 30px; height: 44px;
    background: var(--brand-red); color: var(--card-white);
    display: flex; align-items: center; justify-content: center;
    font-size: 18px;
  }
</style>
</head>
<body>
<main class="sheet">

  <section class="card card--back" aria-label="Card back">
    <div class="brand">MIDAXIS</div>
    <div class="product" style="left:70px; top:250px" role="img" aria-label="Photo of blue welding cart"></div>
    <div class="product" style="left:205px; top:200px" role="img" aria-label="Photo of blue dent puller station"></div>
    <div class="product" style="left:265px; top:300px" role="img" aria-label="Photo of blue spot welder"></div>
    <div class="product" style="left:345px; top:150px" role="img" aria-label="Photo of blue resistance welder"></div>
    <div class="product" style="left:410px; top:250px" role="img" aria-label="Photo of blue repair cart"></div>
    <div class="product" style="left:490px; top:100px" role="img" aria-label="Photo of blue welding unit"></div>
    <div class="product" style="left:555px; top:200px" role="img" aria-label="Photo of handheld riveting tool"></div>
  </section>

  <section class="card card--front" aria-label="Card front">
    <div class="brand">MIDAXIS</div>

    <div class="person">
      <div class="person__name">Daniel Reyes</div>
      <div class="person__role">Manager</div>
    </div>
    <div class="divider"></div>

    <ul class="contacts">
      <li>
        <svg viewBox="0 0 24 24" aria-hidden="true"><path d="M6.6 10.8a15 15 0 0 0 6.6 6.6l2.2-2.2a1 1 0 0 1 1-.25 11.4 11.4 0 0 0 3.6.57 1 1 0 0 1 1 1V20a1 1 0 0 1-1 1A17 17 0 0 1 3 4a1 1 0 0 1 1-1h3.5a1 1 0 0 1 1 1c0 1.25.2 2.45.57 3.57a1 1 0 0 1-.25 1z"/></svg>
        555-010-2100
      </li>
      <li>
        <svg viewBox="0 0 24 24" aria-hidden="true"><path d="M2 5h20v14H2z M3 6l9 7 9-7" fill="none" stroke="#d9262c" stroke-width="2"/></svg>
        yourname@mailbox.com
      </li>
      <li>
        <svg viewBox="0 0 24 24" aria-hidden="true"><circle cx="12" cy="12" r="9" fill="none" stroke="#d9262c" stroke-width="2.5"/><circle cx="12" cy="12" r="3.5"/></svg>
        www.yourwebsite.com
      </li>
    </ul>

    <div class="address-band">Your address, city, state, ZIP 0000</div>
  </section>

</main>
</body>
</html>
```